依頼詳細
弊社ホームページを参考にデザインして頂き干支を入れ
来年以降力を入れていきたい商材(回線事業 ミナモ光)(蓄電池)をどこかに入れたいです
記載項目
(株) ミナモ事務機
530-0047 大阪市北区西天満4-9-22
TEL 06-6418-2275 FAX 06-6418-2276
http://www.minamojimuki.example.jp
希望イメージ
シンプル 複雑
単色 カラフル
暗い 明るい
日常 高級
遊び心 厳粛
未来的 伝統的
女性的 男性的
希望する色
青系
納品ファイル
補足説明
年賀状のデザインをご提案ください
■ 選んだ理由

シンプルで良いデザインでした
社員の投票で最終決定させていただきました

■ 提案者全員のお礼・コメント

沢山ご提案頂きありがとうございました
最後なかなか決めきれず社員の投票になりましたが
素晴らしいご提案がたくさんございました
ありがとうございます。

```html
<!DOCTYPE html>
<html lang="ja">
<head>
<meta charset="utf-8">
<title>ミナモ事務機 年賀状</title>
<link rel="stylesheet" href="https://fonts.googleapis.com/css2?family=Noto+Sans+JP:wght@400;500;700;900&family=Noto+Serif+JP:wght@700;900&display=swap">
<style>
  :root {
    --sky: #5b8ad0;
    --sky-light: #7aa3dd;
    --navy: #2d4b8c;
    --navy-deep: #223a70;
    --gold: #bfa66a;
    --white: #ffffff;
    --ink: #1d1d1d;
    --rule: #333333;
  }
  html, body { margin: 0; padding: 0; overflow: hidden; background: var(--white); }
  .card {
    position: relative;
    width: 809px; height: 1200px;
    overflow: hidden;
    background: var(--white);
    font-family: "Noto Sans JP", sans-serif;
    color: var(--ink);
  }
  .hero {
    position: absolute; left: 0; top: 0;
    width: 809px; height: 690px;
    background: var(--sky);
  }
  .hero-band {
    position: absolute; left: 0; top: 0;
    width: 809px; height: 270px;
    background: var(--sky-light);
  }
  .greeting-column {
    position: absolute; left: 54px; top: 0;
    width: 256px; height: 445px;
    background: var(--navy);
  }
  .geishun {
    position: absolute; left: 70px; top: 60px;
    width: 224px;
    margin: 0;
    font-family: "Noto Serif JP", serif;
    font-weight: 900;
    font-size: 150px;
    line-height: 1.05;
    color: var(--gold);
    text-align: center;
    writing-mode: vertical-rl;
  }
  .offer-circle {
    position: absolute; left: 352px; top: 42px;
    width: 430px; height: 430px;
    border-radius: 50%;
    background: var(--gold);
    z-index: 0;
  }
  .mascot-art {
    position: absolute; left: 400px; top: 300px;
    width: 409px; height: 380px;
    z-index: 1;
  }
  .launch-title {
    position: absolute; right: 28px; top: 66px;
    margin: 0;
    font-weight: 700;
    font-size: 36px;
    letter-spacing: 1px;
    color: var(--white);
    z-index: 2;
  }
  .launch-rule {
    position: absolute; left: 360px; top: 128px;
    width: 425px; height: 2px;
    background: var(--white);
    z-index: 2;
  }
  .offer-box {
    position: absolute; left: 380px; top: 180px;
    width: 362px;
    padding: 14px 14px;
    border: 2px solid var(--white);
    color: var(--white);
    font-weight: 700;
    font-size: 21px;
    line-height: 1.6;
    white-space: nowrap;
    z-index: 2;
  }
  .offer-box p { margin: 0; }
  .message {
    position: absolute; left: 0; top: 690px;
    width: 809px; height: 510px;
  }
  .new-year {
    position: absolute; left: 0; top: 30px;
    width: 809px; margin: 0;
    text-align: center;
    font-weight: 900;
    font-size: 42px;
    letter-spacing: 1px;
  }
  .new-year-rule {
    position: absolute; left: 30px; top: 92px;
    width: 749px; height: 2px;
    background: var(--rule);
  }
  .thanks {
    position: absolute; left: 30px; top: 104px;
    width: 760px; margin: 0;
    font-weight: 500;
    font-size: 28.5px;
    line-height: 1.7;
    letter-spacing: 0.5px;
  }
  .contact {
    position: absolute; left: 42px; top: 240px;
    margin: 0;
    font-style: normal;
    font-size: 24px;
    line-height: 1.75;
    color: #333;
  }
  .contact .row-indent { margin-left: 16px; }
  .contact .gap { display: inline-block; width: 30px; }
  .brand {
    position: absolute; left: 590px; top: 265px;
    width: 200px;
    text-align: center;
    color: var(--navy-deep);
  }
  .brand-mark {
    width: 70px; height: 70px;
    margin: 0 auto 14px;
    background: var(--navy-deep);
  }
  .brand-name {
    font-weight: 700;
    font-size: 36px;
    letter-spacing: 2px;
    line-height: 1.1;
  }
  .brand-sub {
    font-weight: 700;
    font-size: 13px;
    letter-spacing: 1px;
  }
</style>
</head>
<body>
<main class="card">
  <section class="hero">
    <div class="hero-band"></div>
    <div class="greeting-column"></div>
    <h1 class="geishun">迎春</h1>
    <div class="offer-circle"></div>
    <svg class="mascot-art" viewBox="0 0 409 380" role="img" aria-label="干支の蛇を紺色の一本線で描いたイラスト">
      <defs>
        <linearGradient id="mascotTone" x1="0" y1="0" x2="1" y2="1">
          <stop offset="0" stop-color="#2d4b8c" stop-opacity="0.35"/>
          <stop offset="1" stop-color="#223a70" stop-opacity="0.75"/>
        </linearGradient>
      </defs>
      <rect x="20" y="10" width="389" height="360" rx="40" fill="url(#mascotTone)"/>
    </svg>
    <p class="launch-title">回線事業はじめました</p>
    <div class="launch-rule"></div>
    <div class="offer-box">
      <p>『ミナモ光サポートパッケージ』</p>
      <p>回線から通信機器まで</p>
      <p>ワンストップサービス</p>
    </div>
  </section>

  <section class="message">
    <h2 class="new-year">あけましておめでとうございます</h2>
    <div class="new-year-rule"></div>
    <p class="thanks">旧年中は格別のお引き立てを賜り厚く御礼申し上げます。<br>本年も一層のご愛顧の程よろしくお願い申し上げます。</p>
    <address class="contact">
      <span class="company">(株) ミナモ事務機</span><br>
      <span class="row-indent">530-0047　大阪市北区西天満4-9-22</span><br>
      <span class="row-indent">TEL　06-6418-2275<span class="gap"></span>FAX　06-6418-2276</span><br>
      <span class="row-indent">http://www.minamojimuki.example.jp</span>
    </address>
    <div class="brand">
      <div class="brand-mark"></div>
      <div class="brand-name">MINAMO</div>
      <div class="brand-sub">BUSINESS MACHINE</div>
    </div>
  </section>
</main>
</body>
</html>
```